DeedVault Site Introduction and overview Flyer

We need a flyer made that gives an over view of our business. We are a land and mineral records company based in Texas that provides data to many different industries. This should be a bi-fold flyer that measures a 6" x 6" square. The designs should incorporate our company colors with subtle uses of the brighter colors from our new website. Logo and new website pictures are uploaded below.
we would like for the inside left to contain a brief company description: " Since 2005, DeedVault has provided online access to courthouse records and mineral ownership data. Our data, search and order management tools allow you to quickly build and store chains of title, division orders and contact lists. No other website provides as comprehensive of a data set. Start searching DeedVault today.
The front should contain a relevant photo, logo and website name.
the back should contain our contact information and graphic.
the inside right should contain 5 major bullet points with appropriate icons. the bullet points will be:
1. County Courthouse Records Available in Texas, Colorado, New Mexico, and Oklahoma
2. Search all Texas counties at once with Statewide Search
3. Search mineral ownership data from across the State of Texas
4. Download bulk mineral appraisal rolls
5. Plats available in select counties

Target Market(s)
Oil & Gas, Legal, Surveyors, Title, Real Estate, male and female
Industry/Entity Type
Business
Font styles to use
Colors
Designer to choose colors to be used in the design.
Requirements
Must have
- Simplicity.
- relevant colors/graphics

Nice to have
- we would like to have the graphic shown in the sitecapture 2 used, if possible

Should not have
- non-relevant colors, graphics

```html
<!DOCTYPE html>
<html lang="en">
<head>
<meta charset="utf-8">
<title>DeedVault Bi-fold Flyer – Outer Spread</title>
<link rel="stylesheet" href="https://fonts.googleapis.com/css2?family=Lato:wght@400;700&family=Roboto+Condensed:wght@400;700&display=swap">
<style>
  :root {
    --backdrop: #d4d4d4;
    --paper: #ffffff;
    --paper-shade: #f1f1f1;
    --brand-blue: #1f3c9c;
    --sky-top: #0a2ea6;
    --sky-mid: #3d6cd6;
    --sky-low: #7f9fe4;
    --glow: #e0a25a;
    --dusk: #06080f;
    --ink: #1c1c1c;
    --ink-soft: #444;
  }
  * { box-sizing: border-box; margin: 0; padding: 0; }
  html, body { width: 1200px; height: 1200px; overflow: hidden; }
  body {
    background: var(--backdrop);
    display: flex;
    align-items: center;
    justify-content: center;
    font-family: "Lato", sans-serif;
  }
  .spread { display: flex; box-shadow: 0 10px 30px rgba(0,0,0,.18); }
  .panel {
    position: relative;
    width: 560px;
    height: 560px;
    background: linear-gradient(160deg, var(--paper) 0%, var(--paper-shade) 100%);
    overflow: hidden;
  }

  /* Back cover */
  .back-landscape {
    position: absolute; left: 0; top: 0; width: 100%; height: 390px;
    background:
      radial-gradient(ellipse 55% 22% at 28% 88%, rgba(70,70,70,.45), transparent 70%),
      radial-gradient(ellipse 45% 18% at 78% 80%, rgba(80,80,80,.35), transparent 70%),
      linear-gradient(180deg,
        var(--paper) 0%, #f2f2f2 12%,
        #cfcfcf 22%, #a9a9a9 30%, #bdbdbd 38%,
        #8f8f8f 46%, #9c9c9c 60%, #858585 78%, #7a7a7a 100%);
  }
  .back-rule { position: absolute; left: 0; top: 390px; width: 100%; height: 4px; background: var(--brand-blue); }
  .contact-list {
    position: absolute; left: 36px; top: 424px; list-style: none;
    font-size: 13px; color: var(--ink); line-height: 1.55;
  }
  .contact-list li { display: flex; align-items: center; gap: 9px; }
  .contact-list .phone { font-weight: 700; font-size: 15px; }
  .contact-list svg { width: 11px; height: 11px; fill: var(--brand-blue); flex: none; }
  .address {
    position: absolute; left: 300px; top: 428px; display: flex; gap: 9px;
    font-size: 12.5px; color: var(--ink-soft); line-height: 1.4;
  }
  .address svg { width: 10px; height: 14px; fill: var(--brand-blue); flex: none; margin-top: 2px; }
  .address strong { color: var(--ink); font-weight: 700; }

  /* Front cover */
  .brand {
    position: absolute; left: 0; right: 0; top: 62px;
    display: flex; justify-content: center; align-items: center; gap: 8px;
    font-family: "Roboto Condensed", sans-serif; font-weight: 700;
    font-size: 30px; color: var(--brand-blue); letter-spacing: .5px;
  }
  .brand-mark { width: 14px; height: 14px; background: var(--brand-blue); }
  .site-url {
    position: absolute; right: 34px; top: 140px;
    font-size: 12px; letter-spacing: 3px; color: var(--ink);
  }
  .cover-photo {
    position: absolute; left: 0; top: 166px; width: 100%; height: 394px;
    background:
      radial-gradient(ellipse 40% 14% at 42% 76%, rgba(224,162,90,.85), transparent 70%),
      radial-gradient(ellipse 70% 40% at 15% 100%, rgba(6,8,15,.95), transparent 75%),
      linear-gradient(180deg,
        var(--sky-top) 0%, #1b47c0 25%, var(--sky-mid) 50%,
        var(--sky-low) 66%, #4a5f9c 73%,
        #1a2140 82%, var(--dusk) 100%);
  }
  .headline {
    position: absolute; right: 34px; bottom: 38px; text-align: right;
    font-family: "Roboto Condensed", sans-serif; color: var(--paper);
    line-height: 1.02; text-transform: uppercase;
    text-shadow: 0 2px 6px rgba(0,0,0,.35);
  }
  .headline .lead { font-weight: 700; font-size: 38px; }
  .headline .sub { font-weight: 400; font-size: 32px; }
</style>
</head>
<body>
  <main class="spread">
    <section class="panel back-cover">
      <div class="back-landscape" role="img" aria-label="Grayscale photo of a rocky Texas mesa with desert grass in the foreground"></div>
      <div class="back-rule"></div>
      <ul class="contact-list">
        <li class="phone">
          <svg viewBox="0 0 24 24"><path d="M6.6 10.8a15.1 15.1 0 0 0 6.6 6.6l2.2-2.2a1 1 0 0 1 1-.25 11.4 11.4 0 0 0 3.6.57 1 1 0 0 1 1 1V20a1 1 0 0 1-1 1A17 17 0 0 1 3 4a1 1 0 0 1 1-1h3.5a1 1 0 0 1 1 1c0 1.25.2 2.45.57 3.6a1 1 0 0 1-.25 1z"/></svg>
          +41 44 555 0182
        </li>
        <li>
          <svg viewBox="0 0 24 24"><path d="M2 5h20v14H2zm2 2v.5l8 5 8-5V7z"/></svg>
          contact@northfieldlandholdings.com
        </li>
        <li>
          <svg viewBox="0 0 24 24"><circle cx="12" cy="12" r="10"/></svg>
          www.northfieldlandholdings.com
        </li>
      </ul>
      <div class="address">
        <svg viewBox="0 0 20 28"><path d="M10 0a10 10 0 0 0-10 10c0 7.5 10 18 10 18s10-10.5 10-18A10 10 0 0 0 10 0zm0 14a4 4 0 1 1 0-8 4 4 0 0 1 0 8z"/></svg>
        <p><strong>Northfield Land Holdings Ltd.</strong><br>c/o Corvane Advisory Services SA<br>Lindenweg 24, CH-8002 Zurich<br>Switzerland</p>
      </div>
    </section>

    <section class="panel front-cover">
      <div class="brand"><span class="brand-mark"></span>DeedVault</div>
      <p class="site-url">www.deedvault.com</p>
      <div class="cover-photo" role="img" aria-label="Silhouettes of oil pump jacks against a deep blue sky at sunset"></div>
      <h1 class="headline">
        <span class="lead">Start Your Search</span><br>
        <span class="sub">No Obligation</span><br>
        <span class="sub">Free Searching</span>
      </h1>
    </section>
  </main>
</body>
</html>
```